Solar panel cleaning flyer design.

I'm looking for a flyer design for my new company called Brightfield Panel Works. We are a South Australian company that professionally clean residential and commercial solar panels. We generate leads by going door to door and need a flyer to hand out to our customers if they are interested in our service. As we are a new company we don't have anything particular in mind so be creative! Must include the company name and logo.

```html
<!DOCTYPE html>
<html lang="en">
<head>
<meta charset="utf-8">
<title>Brightfield Panel Works – Solar Panel Cleaning Flyer</title>
<link rel="stylesheet" href="https://fonts.googleapis.com/css2?family=Montserrat:wght@600;700;800&family=Open+Sans:wght@400;600;700&display=swap">
<style>
  :root {
    --navy: #26333f;
    --blue: #1d87c9;
    --blue-deep: #136aa6;
    --green: #5bb531;
    --ink: #333a40;
    --muted: #6b7278;
    --white: #ffffff;
    --sky-top: #cfe3f2;
    --panel: #2c4f86;
  }
  * { box-sizing: border-box; margin: 0; padding: 0; }
  html, body { width: 900px; height: 1200px; overflow: hidden; background: var(--white); }
  body { font-family: "Open Sans", Arial, sans-serif; color: var(--ink); }

  .flyer { position: relative; width: 900px; height: 1200px; background: var(--white); overflow: hidden; }

  .header { position: absolute; top: 0; left: 0; right: 0; height: 170px; display: flex; align-items: center; justify-content: space-between; padding: 0 60px; }
  .brand { display: flex; align-items: center; gap: 18px; }
  .brand-dot { width: 62px; height: 62px; border-radius: 50%; background: var(--blue); }
  .brand-name { font-family: "Montserrat", Arial, sans-serif; font-weight: 800; font-size: 36px; color: var(--navy); line-height: 1.05; width: 330px; }
  .site-url { font-family: "Open Sans", Arial, sans-serif; font-weight: 600; font-size: 21px; color: var(--navy); }

  .title-band { position: absolute; top: 178px; left: 0; right: 0; height: 110px; background: var(--navy); display: flex; align-items: center; justify-content: center; text-align: center; }
  .title-band h1 { font-family: "Montserrat", Arial, sans-serif; font-weight: 800; font-size: 30px; line-height: 1.3; color: var(--white); text-transform: uppercase; letter-spacing: 0.3px; }

  .hero-photo { position: absolute; top: 288px; left: 0; right: 0; height: 300px; background: linear-gradient(180deg, var(--sky-top) 0%, #e8eff4 35%, #6f8fb8 55%, var(--panel) 100%); }

  .intro-band { position: absolute; top: 588px; left: 0; right: 0; height: 150px; background: var(--blue); display: flex; align-items: center; justify-content: center; padding: 0 70px; text-align: center; }
  .intro-band p { color: var(--white); font-size: 21px; line-height: 1.45; }

  .services { position: absolute; top: 770px; left: 60px; width: 400px; }
  .section-title { font-family: "Montserrat", Arial, sans-serif; font-weight: 800; font-size: 28px; color: var(--navy); text-transform: uppercase; margin-bottom: 14px; }
  .section-title span { color: var(--blue); }
  .services p { font-size: 16px; line-height: 1.6; color: var(--muted); }

  .work-photo { position: absolute; top: 770px; left: 500px; width: 400px; height: 330px; background: linear-gradient(180deg, #9ccbe9 0%, #5e8fc4 50%, var(--panel) 100%); }

  .call-badge { position: absolute; top: 810px; left: 515px; width: 180px; height: 180px; border-radius: 50%; background: var(--blue); border: 6px solid var(--white); display: flex; flex-direction: column; align-items: center; justify-content: center; color: var(--white); text-align: center; }
  .call-badge strong { font-family: "Montserrat", Arial, sans-serif; font-weight: 800; font-size: 24px; text-transform: uppercase; }
  .call-badge span { font-weight: 700; font-size: 19px; margin-top: 4px; }

  .contact { position: absolute; top: 990px; left: 60px; }
  .contact-list { list-style: none; }
  .contact-list li { display: flex; align-items: center; gap: 12px; font-size: 17px; color: var(--ink); margin-bottom: 8px; }
  .contact-list svg { width: 22px; height: 22px; flex: none; }

  .footer-wave { position: absolute; left: 0; bottom: 0; width: 900px; height: 90px; }
</style>
</head>
<body>
<div class="flyer">
  <header class="header">
    <div class="brand">
      <div class="brand-dot"></div>
      <div class="brand-name">Brightfield Panel Works</div>
    </div>
    <div class="site-url">www.brightfieldpanel.com.au</div>
  </header>

  <div class="title-band">
    <h1>Professionally clean residential<br>and commercial solar panels</h1>
  </div>

  <div class="hero-photo" role="img" aria-label="Workers cleaning a large field of rooftop solar panels under a clear sky"></div>

  <div class="intro-band">
    <p>We are a South Australian company that professionally clean residential and commercial solar panels. We generate leads by going door to door and need a flyer to hand out to our customers if they are interested in our service.</p>
  </div>

  <section class="services">
    <h2 class="section-title">What <span>we do?</span></h2>
    <p>Our trained crew washes rooftop and ground mounted arrays with pure water and soft brushes, removing dust, bird droppings and grime that cut output. We work safely at height, leave no marks behind and send you a short report on every panel we clean.</p>
  </section>

  <div class="work-photo" role="img" aria-label="Technician on a roof washing solar panels"></div>

  <div class="call-badge">
    <strong>Call now!</strong>
    <span>0400 518 276</span>
  </div>

  <section class="contact">
    <h2 class="section-title">Contact <span>us:</span></h2>
    <ul class="contact-list">
      <li>
        <svg viewBox="0 0 24 24"><circle cx="12" cy="12" r="12" fill="#1d87c9"/><path d="M8.5 6.5l2 2-1.2 1.6c.8 1.7 2 2.9 3.6 3.6l1.6-1.2 2 2-1.3 1.8c-4.2-.4-7.9-4.1-8.3-8.3z" fill="#fff"/></svg>
        0400 518 276
      </li>
      <li>
        <svg viewBox="0 0 24 24"><circle cx="12" cy="12" r="12" fill="#1d87c9"/><rect x="6" y="8" width="12" height="8" rx="1" fill="#fff"/><path d="M6.5 8.5l5.5 4 5.5-4" stroke="#1d87c9" stroke-width="1.2" fill="none"/></svg>
        hello@brightfieldpanel.com.au
      </li>
      <li>
        <svg viewBox="0 0 24 24"><circle cx="12" cy="12" r="12" fill="#1d87c9"/><circle cx="12" cy="12" r="6" stroke="#fff" stroke-width="1.4" fill="none"/><path d="M6 12h12M12 6c-2.5 3-2.5 9 0 12M12 6c2.5 3 2.5 9 0 12" stroke="#fff" stroke-width="1.2" fill="none"/></svg>
        www.brightfieldpanel.com.au
      </li>
    </ul>
  </section>

  <svg class="footer-wave" viewBox="0 0 900 90" preserveAspectRatio="none" aria-hidden="true">
    <path d="M0 40 C250 90 600 0 900 30 L900 90 L0 90 Z" fill="#5bb531"/>
    <path d="M0 60 C300 100 600 20 900 50 L900 90 L0 90 Z" fill="#1d87c9"/>
  </svg>
</div>
</body>
</html>
```